Lab & Medical Equipment Repair Company Business Card Design

Looking for business card design for a lab & medical equipment repair company. Must be double-sided and must list our primary pieces we repair. Optionally, can include a QR code which should direct to our website.

Clients are usually doctors, so the card must be designed with a professional tone; however, we are looking for creativity in presentation. Open as to what should be on the front and back on card.

** Looking for a CLEAN design with creativity. Please use "Nice to have Priorities" items with discretion.

Core marketing logic:

When lab or medical equipment needs repair, most doctors call the manufacturers and schedule a technician to repair. Usually this takes one or two weeks, and, often, their work spoils. Alternatively, the doctors could hold equipment insurance which gives them a less expensive cost, but the response time is still similarly long.

Our company provides both competitive rates and one of the fastest response times in the industry. Technicians are dispatched directly to the site of the equipment, usually within 24 hours. Equipment under contract receives the same fast response time and includes complimentary annual maintenance. We service some of the most prestigious facilities in the Pittsburgh area and cover all of Western Pennsylvania, Ohio, and West Virginia.

Target Market(s)

Laboratory owners (doctors)

Industry/Entity Type

Marketing

Requirements
Must have
• Company Logo
Employee Name: Ray Dunwoody
Employee Title: CEO
Company Phone: 724-555-0187
Company Fax: 866-555-0143
Company Address: PO Box 518 Harmony Glen, PA 16099
Company Website: www.brightfixlabtech.example
Equipment We Service: Freezers, Cryostorage, Incubators, Centrifuges, Refrigerators, Environmental Chambers, Autoclaves, and more.

Nice to have
• Company Facebook: facebook.com/bfltllc
Company Twitter: @BFLTLLC
QR Code (link to website): www.brightfixlabtech.example

```html
<!DOCTYPE html>
<html lang="en">
<head>
<meta charset="utf-8">
<title>BFLT Business Card</title>
<link href="https://fonts.googleapis.com/css2?family=Arimo:ital,wght@0,400;0,700;1,400&display=swap" rel="stylesheet">
<style>
  :root {
    --green-light: #8cc63f;
    --green-mid: #5fae35;
    --green-dark: #3a8a26;
    --ink: #1a1a1a;
    --grey-text: #555555;
    --rule-green: #3f9b34;
    --paper: #ffffff;
    --backdrop: #e9e9e6;
  }
  * { box-sizing: border-box; margin: 0; padding: 0; }
  html, body { width: 1200px; height: 750px; overflow: hidden; }
  body {
    background: var(--backdrop);
    font-family: "Arimo", Arial, sans-serif;
    position: relative;
  }
  .card {
    position: absolute;
    top: 211px;
    width: 540px;
    height: 328px;
    background: var(--paper);
    overflow: hidden;
    box-shadow: 0 2px 8px rgba(0,0,0,0.18);
  }
  .card--front { left: 45px; border: 1px solid #9a9a9a; }
  .card--back { left: 615px; }

  .green-field {
    background:
      radial-gradient(ellipse 70% 120% at 20% -10%, rgba(255,255,255,0.28), rgba(255,255,255,0) 60%),
      linear-gradient(160deg, var(--green-light) 0%, var(--green-mid) 55%, var(--green-dark) 100%);
  }
  .front__panel {
    position: absolute; left: 0; top: 0; width: 240px; height: 100%;
    display: flex; flex-direction: column; align-items: center; justify-content: center;
  }
  .brand-name {
    font-family: "Arimo", Arial, sans-serif;
    font-weight: 700;
    color: var(--ink);
    letter-spacing: 6px;
    display: flex; align-items: center; gap: 10px;
  }
  .brand-name__mark { width: 14px; height: 14px; background: var(--rule-green); display: inline-block; }
  .front__panel .brand-name { font-size: 46px; margin-top: -14px; }
  .front__panel .brand-name__mark { background: var(--paper); }
  .tagline {
    font-weight: 700; font-size: 13px; text-align: center; line-height: 1.4;
    color: var(--paper); margin-top: 10px; letter-spacing: 0.2px;
  }

  .front__details {
    position: absolute; left: 240px; top: 0; right: 0; height: 100%;
    text-align: right; padding-right: 16px;
  }
  .person-name {
    position: absolute; right: 16px; top: 138px;
    font-size: 26px; font-weight: 700; color: #444;
  }
  .name-rule {
    position: absolute; left: 0; right: 0; top: 171px;
    height: 1px; background: var(--rule-green);
  }
  .person-title {
    position: absolute; right: 16px; top: 178px;
    font-size: 25px; font-style: italic; color: #444;
  }
  .contact-list {
    position: absolute; right: 16px; top: 226px;
    list-style: none; font-size: 14.5px; line-height: 22px; color: var(--grey-text);
  }

  .back__top { position: absolute; left: 0; top: 0; width: 100%; height: 100px; }
  .back__middle {
    position: absolute; left: 0; top: 100px; width: 100%; height: 128px;
    display: flex; flex-direction: column; align-items: center; justify-content: center;
  }
  .back__middle .brand-name { font-size: 54px; }
  .back__middle .tagline { color: #333; font-size: 13.5px; margin-top: 8px; }
  .back__bottom {
    position: absolute; left: 0; top: 228px; width: 100%; height: 100px;
    background: linear-gradient(180deg, var(--green-mid), var(--green-dark));
    color: var(--paper); text-align: center; font-size: 14px; line-height: 18px;
    padding-top: 14px;
  }
  .services__heading { font-weight: 700; }
</style>
</head>
<body>
  <section class="card card--front">
    <div class="front__panel green-field">
      <div class="brand-name"><span>BFLT</span><span class="brand-name__mark"></span></div>
      <p class="tagline">LAB &amp; MEDICAL EQUIPMENT<br>REPAIR</p>
    </div>
    <div class="front__details">
      <h1 class="person-name">Ray Dunwoody</h1>
      <div class="name-rule"></div>
      <p class="person-title">CEO</p>
      <ul class="contact-list">
        <li>PO Box 518 Harmony Glen, PA 16099</li>
        <li>Phone: 724-555-0187</li>
        <li>Fax: 866-555-0143</li>
        <li>www.brightfixlabtech.example</li>
      </ul>
    </div>
  </section>

  <section class="card card--back">
    <div class="back__top green-field"></div>
    <div class="back__middle">
      <div class="brand-name"><span>BFLT</span><span class="brand-name__mark"></span></div>
      <p class="tagline">LAB &amp; MEDICAL EQUIPMENT REPAIR</p>
    </div>
    <div class="back__bottom services">
      <p class="services__heading">We Service:</p>
      <p>Freezers - Cryostorage - Incubators - Centrifuges - Refrigerators</p>
      <p>Environmental Chambers - Autoclaves</p>
      <p>and more ...</p>
    </div>
  </section>
</body>
</html>
```